Pharma Business needs a new careers template

We need a new job posting template to use for all of our open positions. We are in the pharma production business and want to elevate our job postings. The design should incorporate our company colours (namely blue and white).<br/><br/>The completed work should look professional, innovative and slightly quirky.<br/><br/>Feel free to familiarise yourself with some of our current designs on our website (www.torvax.com).<br/><br/>We have a few ideas of how we want the template to look like:<br/><br/>- We would like the design to incorporate various boxes that show different information like "Role Profile", "Benefits" etc.<br/><br/>- We would like to show some of our achievements in a special type of ellipses that remind of tablets or capsules. See a close example of another job posting incorporating similar design (but with circles instead of capsules/tablets) attached.<br/><br/>- We would like some of the main information like job location, contact phone etc to be shown after a corresponding icon. Example screenshot applied.<br/><br/>We have also attached an example job posting to give you an idea of what information our template should hold.

Industry/Entity Type

Pharmaceutical

Colors
33a6d7
ffffff
0393ce
3277b5

Requirements
Must have
• The file should be editable so we can freely fill it for each new position. We should also have it in PSD format.

```html
<!DOCTYPE html>
<html lang="en">
<head>
<meta charset="utf-8">
<title>Torvax Pharma – Job Posting</title>
<link rel="stylesheet" href="https://fonts.googleapis.com/css2?family=Lato:ital,wght@0,400;0,700;1,400&family=Montserrat:wght@500;700&display=swap">
<style>
  :root {
    --blue-dark: #1a5ba8;
    --blue-light: #a6d6f6;
    --ink: #2b2b2b;
    --text: #2a2a2a;
    --white: #ffffff;
    --pill-low: #e3e3e5;
  }
  * { box-sizing: border-box; margin: 0; padding: 0; }
  html, body { width: 902px; height: 1200px; overflow: hidden; background: var(--white); }
  .flyer { position: relative; width: 902px; height: 1200px; background: var(--white); overflow: hidden; font-family: "Lato", sans-serif; color: var(--text); }
  .header-wave, .footer-wave { position: absolute; left: 0; width: 902px; }
  .header-wave { top: 0; height: 200px; }
  .footer-wave { top: 1040px; height: 160px; }
  .brand { position: absolute; left: 70px; top: 42px; width: 140px; text-align: center; font-family: "Montserrat", sans-serif; font-weight: 700; color: var(--blue-dark); }
  .brand-name { display: block; font-size: 38px; line-height: 1; letter-spacing: 0.5px; }
  .brand-sub { display: block; font-size: 15px; letter-spacing: 2px; margin-top: 8px; }
  .job-title { position: absolute; left: 324px; top: 30px; font-family: "Montserrat", sans-serif; font-weight: 500; font-size: 40px; color: var(--white); letter-spacing: 0.5px; }
  .intro { position: absolute; left: 82px; top: 146px; width: 780px; font-size: 12.2px; line-height: 14.6px; }
  .capsule { position: absolute; left: 41px; width: 820px; height: 200px; }
  .capsule svg { position: absolute; inset: 0; width: 820px; height: 200px; overflow: visible; }
  .capsule-heading { position: absolute; font-family: "Montserrat", sans-serif; font-weight: 700; color: var(--ink); text-transform: uppercase; }
  .capsule-heading.large { font-size: 32px; line-height: 46px; }
  .capsule-heading.small { font-size: 19px; line-height: 27px; }
  .capsule-text { position: absolute; font-size: 13.2px; line-height: 15.6px; text-align: justify; }
  .bullets { position: absolute; list-style: none; font-style: italic; font-size: 10.5px; }
  .bullets li { position: relative; height: 22.6px; line-height: 16px; padding-left: 26px; }
  .bullets li::before { content: ""; position: absolute; left: 0; top: 4px; width: 9px; height: 9px; border-radius: 50%; background: var(--blue-dark); }
  .role { top: 256px; }
  .success { top: 466px; }
  .benefits { top: 676px; }
  .challenge { top: 882px; }
  .location { position: absolute; left: 100px; top: 1108px; }
  .location h3 { font-family: "Montserrat", sans-serif; font-weight: 700; font-size: 17px; color: var(--blue-dark); margin-bottom: 12px; }
  .address { display: flex; align-items: center; gap: 12px; font-size: 12.5px; line-height: 16px; }
  .contact { position: absolute; left: 0; top: 1124px; width: 902px; color: var(--white); font-family: "Montserrat", sans-serif; font-weight: 700; }
  .contact h3 { position: absolute; left: 443px; top: 0; font-size: 17px; }
  .contact-item { position: absolute; top: 33px; display: flex; align-items: center; gap: 8px; font-size: 17px; }
  .contact-item.phone { left: 408px; }
  .contact-item.email { left: 610px; font-weight: 500; }
</style>
</head>
<body>
<main class="flyer">

  <svg class="header-wave" viewBox="0 0 902 200" aria-hidden="true">
    <path fill="var(--blue-light)" d="M250 56 C300 104 380 118 450 121 C560 126 640 112 720 107 C800 102 860 122 902 162 V122 C860 106 800 98 720 102 C620 108 540 122 440 115 C360 108 300 92 250 56Z"/>
    <path fill="var(--blue-dark)" d="M197 0 H902 V104 C840 108 780 90 700 98 C600 110 520 114 420 104 C330 94 282 76 257 52 C232 28 212 10 197 0Z"/>
  </svg>

  <div class="brand"><span class="brand-name">torvax</span><span class="brand-sub">PHARMA</span></div>
  <h1 class="job-title">JOB TITLE</h1>

  <p class="intro">Habitasse porta luctus porta. Aptent augue. Justo aliquet urna justo. Inceptos ligula elit aenean maecenas montes ullamcorper commodo volutpat Massa aliquam velit interdum viverra congue malesuada lacus lobortis egestas malesuada blandit nec facilisis. Fermentum tempor arcu litora fringilla, quis aenean sagittis feugiat a pretium hendrerit sociosqu mattis, maecenas.<br>Turpis lorem. Aliquet nibh sociis mus facilisi interdum aliquet aenean sem vulputate natoque. Malesuada rutrum sociosqu sociosqu litora nunc ornare feugiat volutpat feugiat natoque dictumst scelerisque sociis ornare Eget inceptos quam interdum.</p>

  <svg width="0" height="0" aria-hidden="true">
    <defs>
      <linearGradient id="pillFill" x1="0" y1="0" x2="0" y2="1">
        <stop offset="0" stop-color="#ffffff"/>
        <stop offset="1" stop-color="#e3e3e5"/>
      </linearGradient>
      <filter id="pillShadow" x="-5%" y="-10%" width="110%" height="130%">
        <feDropShadow dx="0" dy="5" stdDeviation="5" flood-color="#000" flood-opacity="0.22"/>
      </filter>
    </defs>
  </svg>

  <section class="capsule role">
    <svg viewBox="0 0 820 200" aria-hidden="true">
      <rect x="10" y="18" width="800" height="174" rx="87" fill="url(#pillFill)" filter="url(#pillShadow)"/>
      <path fill="var(--blue-dark)" fill-rule="evenodd" d="M265 0 H95 A95 95 0 0 0 95 190 H320 L290 162 H100 A67 67 0 0 1 100 28 H265Z"/>
    </svg>
    <h2 class="capsule-heading large" style="left:81px; top:47px;">Role<br>Profile:</h2>
    <p class="capsule-text" style="left:296px; top:38px; width:494px;">Velit Commodo, ultrices proin tellus montes magnis mi porttitor metus sociis condimentum dis platea. Ad consectetuer laoreet euismod ad donec tellus elit ad metus lectus. Sit pretium quis imperdiet velit turpis diam urna torquent ante phasellus nascetur per euismod ultrices consectetuer a. Sollicitudin lobortis scelerisque vel senectus id, pharetra iaculis non sem id nam odio fames facilisi quam integer condimentum rutrum pulvinar inceptos. Montes id nonummy platea, mattis proin cum.</p>
  </section>

  <section class="capsule success">
    <svg viewBox="0 0 820 200" aria-hidden="true">
      <rect x="0" y="18" width="790" height="174" rx="87" fill="url(#pillFill)" filter="url(#pillShadow)"/>
      <g transform="translate(820 0) scale(-1 1)">
        <path fill="var(--blue-light)" fill-rule="evenodd" d="M265 0 H95 A95 95 0 0 0 95 190 H320 L290 162 H100 A67 67 0 0 1 100 28 H265Z"/>
      </g>
    </svg>
    <ul class="bullets" style="left:81px; top:20px;">
      <li>Cubilia. Porta. Morbi aliquet aptent Aenean nostra purus.</li>
      <li>Rhoncus vitae mus fermentum placerat placerat libero.</li>
      <li>Interdum, dapibus aliquet dignissim hac fusce non. Consectetuer.</li>
      <li>Quam hac, ornare hendrerit ultricies.</li>
      <li>Netus parturient elementum, nisi purus dui.</li>
      <li>Justo sodales, suspendisse fermentum, quisque fermentum quisque pulvinar.</li>
      <li>Convallis lectus feugiat suspendisse ullamcorper nonummy duis pretium.</li>
      <li>Eget pretium per tempor natoque. Quisque.</li>
    </ul>
    <h2 class="capsule-heading small" style="left:543px; top:60px;">To be successful<br>in this role you<br>should have:</h2>
  </section>

  <section class="capsule benefits">
    <svg viewBox="0 0 820 200" aria-hidden="true">
      <rect x="10" y="18" width="806" height="174" rx="87" fill="url(#pillFill)" filter="url(#pillShadow)"/>
      <path fill="var(--blue-dark)" fill-rule="evenodd" d="M265 0 H95 A95 95 0 0 0 95 190 H320 L290 162 H100 A67 67 0 0 1 100 28 H265Z"/>
    </svg>
    <h2 class="capsule-heading large" style="left:81px; top:71px;">Benefits:</h2>
    <ul class="bullets" style="left:343px; top:34px;">
      <li>Nonummy fermentum nec dictumst et.</li>
      <li>Venenatis. Aenean ac. Commodo volutpat dolor libero mus.</li>
      <li>Cras consequat, non tempor justo.</li>
      <li>Natoque potenti Hymenaeos ad tristique torquent ultrices. Nec donec. Eu.</li>
      <li>Ac consequat ridiculus convallis curae; porttitor.</li>
      <li>Lobortis non hendrerit taciti sed. Cursus.</li>
    </ul>
  </section>

  <section class="capsule challenge">
    <svg viewBox="0 0 820 200" aria-hidden="true">
      <rect x="0" y="18" width="790" height="174" rx="87" fill="url(#pillFill)" filter="url(#pillShadow)"/>
      <g transform="translate(820 0) scale(-1 1)">
        <path fill="var(--blue-light)" fill-rule="evenodd" d="M265 0 H95 A95 95 0 0 0 95 190 H320 L290 162 H100 A67 67 0 0 1 100 28 H265Z"/>
      </g>
    </svg>
    <p class="capsule-text" style="left:54px; top:40px; width:484px;">Curae; eros cubilia suspendisse netus turpis laoreet nonummy vivamus scelerisque rutrum.<br>Risus porttitor semper erat lorem ante orci cum natoque mauris lobortis. Velit semper aliquet. Metus proin ullamcorper augue urna. Eros taciti maecenas est, aliquam parturient etiam gravida nullam molestie. Sem imperdiet. Porta praesent sit. Vitae pede luctus et potenti ac augue primis cum vel. Blandit scelerisque tincidunt tincidunt luctus pretium eleifend.</p>
    <h2 class="capsule-heading small" style="left:567px; top:62px;">Challenged by<br>this career<br>opportunity?</h2>
  </section>

  <svg class="footer-wave" viewBox="0 0 902 160" aria-hidden="true">
    <path fill="var(--blue-dark)" d="M334 160 C346 110 392 72 458 66 C560 57 660 74 762 63 C784 26 830 2 868 8 C888 12 902 28 902 38 V160Z"/>
  </svg>

  <div class="location">
    <h3>JOB LOCATION</h3>
    <div class="address">
      <svg width="14" height="20" viewBox="0 0 14 20" aria-hidden="true"><path fill="var(--blue-dark)" d="M7 0 A7 7 0 0 0 0 7 C0 12 7 18 7 18 C7 18 14 12 14 7 A7 7 0 0 0 7 0Z M7 4 A3 3 0 1 1 7 10 A3 3 0 1 1 7 4Z"/><rect x="1" y="18.5" width="12" height="1.5" rx="0.75" fill="var(--blue-dark)"/></svg>
      <span>48 Maren Str.<br>1420 Delvo, Bulgaria</span>
    </div>
  </div>

  <div class="contact">
    <h3>Contact Us :</h3>
    <div class="contact-item phone">
      <svg width="16" height="16" viewBox="0 0 16 16" aria-hidden="true"><circle cx="8" cy="8" r="7" fill="none" stroke="#fff" stroke-width="1.5"/><path fill="#fff" d="M5.2 4.2 L6.6 4 L7.2 5.8 L6.3 6.6 C6.7 7.6 7.5 8.5 8.6 9 L9.4 8.1 L11.2 8.7 L11 10.2 C8 10.4 5 7.5 5.2 4.2Z"/></svg>
      <span>+359 2 41 63 508</span>
    </div>
    <div class="contact-item email">
      <svg width="16" height="12" viewBox="0 0 16 12" aria-hidden="true"><rect x="0.5" y="0.5" width="15" height="11" fill="#fff"/><path d="M1 1 L8 7 L15 1" fill="none" stroke="var(--blue-dark)" stroke-width="1.3"/></svg>
      <span>office@torvax.com</span>
    </div>
  </div>

</main>
</body>
</html>
```